Broschüre Premium Kunstrasen
Der gesamte Auftrag wurde perfekt von Carola begleitet und abgewickelt. Prima Zusammenarbeit - ohne Wenn und Aber. Alles wurde zügig bearbeitet, sodass unsere 16-Seiten Broschüre innerhalb kurzer Zeit fertiggestellt war. Wir sind 100% zufrieden!!
Zielgruppe
Hauptsächlich (70% unserer Tätigkeit) verlegen wir Premium Kunstrasen in Gärten von Privatleuten. Schlüsselfertig .
Unsere Auftraggeber in diesem Bereich sind in der Regel zwischen 40 bis 70 Jahre alt und gut situiert.
30% unserer Tätigkeit besteht aus der reinen Lieferung von hochwertigen Kunstrasen für den Balkon, Terrasse.
Unsere Produkte haben lange Garantiezeiten von 15 Jahren. Deshalb nennen wir unsere Produkte auch Halmvollio
Aufgabenstellung
Die Broschüre wird beim Versand einer Musterbox mitgeschickt und soll ein Format von 210x210 haben.
In der Broschüre werden mehrere Produkte mit ihren technischen Eigenschaften und dem Preis abgebildet.
Die Produkte sollen in eine Story von Bildern und Texten eingebettet sein.
Die Broschüre soll aus ca. 12-16 Seiten bestehen. Dabei sollen die Texte unserer alten Broschüre übernommen werden, ebenso wie die Texte aus der Datei text 1 broschüre 2023. Wir können uns vorstellen das unsere Kunstrasensorten und die dazugehörige Beschreibung im Zusammenhang mit den ausgeführten Projekten stehen (sh. Beispiel velum sod.at). Die Fotos zu den Projekten werden wir noch uploaden.

```html
<!DOCTYPE html>
<html lang="de">
<head>
<meta charset="utf-8">
<title>Halmvollio Broschüre – Verda</title>
<link href="https://fonts.googleapis.com/css2?family=Nunito+Sans:wght@300;400;600;800&display=swap" rel="stylesheet">
<style>
  :root {
    --green-dark: #3a5d38;
    --green-text: #3f5a3d;
    --label: #8b9c89;
    --dot-1: #3d6a3a;
    --dot-2: #6aa852;
    --dot-3: #9b9d3b;
    --dot-4: #a7996b;
    --icon-grey: #b5c0b3;
    --white: #ffffff;
    --rule: #ffffff;
  }
  * { box-sizing: border-box; margin: 0; padding: 0; }
  html, body { width: 1200px; height: 600px; overflow: hidden; background: var(--white); }
  body { font-family: "Nunito Sans", Arial, sans-serif; color: var(--green-text); }
  .spread { position: relative; width: 1200px; height: 600px; overflow: hidden; }

  /* Left page */
  .page-left { position: absolute; left: 0; top: 0; width: 600px; height: 600px; background: var(--white); }
  .hero-pool {
    position: absolute; left: 0; top: 0; width: 600px; height: 197px;
    background: linear-gradient(100deg, #3f9bd0 0%, #5fb8e2 35%, #c9a38a 55%, #b89880 65%, #5d8a2c 80%, #4a7424 100%);
  }
  .brand-seal {
    position: absolute; left: 270px; top: 156px; width: 82px; height: 82px;
    border-radius: 50%; background: var(--white); border: 2px solid var(--dot-2);
    display: flex; align-items: center; justify-content: center;
    font-weight: 800; font-size: 12px; color: var(--dot-2);
  }
  .spec-label { position: absolute; left: 29px; font-size: 11.5px; font-weight: 600; color: var(--label); }
  .spec-value { position: absolute; font-size: 11.5px; color: var(--green-text); }
  .colour-dots { position: absolute; left: 29px; top: 280px; display: flex; gap: 6px; }
  .colour-dots span { width: 22.5px; height: 22.5px; border-radius: 50%; }
  .use-list { position: absolute; left: 29px; top: 340px; list-style: none; font-size: 11.5px; line-height: 14.5px; }
  .use-list li::before { content: "•"; margin-right: 4px; }
  .pile-icon { position: absolute; left: 28px; top: 431px; }
  .pile-art { position: absolute; left: 35px; top: 434px; width: 25px; height: 32px; background: linear-gradient(to top, #b9c3b7, #dde3dc); border-radius: 40% 40% 2px 2px; }
  .weight-icon { position: absolute; left: 29px; top: 497px; }

  .badge-plain { position: absolute; left: 507px; top: 219px; width: 60px; height: 60px; border-radius: 50%; border: 3px solid #8a958a; background: #eef0ee; }
  .title-bar { position: absolute; left: 215px; top: 263px; width: 8px; height: 60px; background: var(--green-dark); }
  .product-name { position: absolute; left: 235px; top: 261px; font-size: 38px; font-weight: 800; color: var(--green-dark); letter-spacing: 0.5px; line-height: 1; }
  .product-claim { position: absolute; left: 236px; top: 306px; font-size: 17.5px; font-weight: 800; color: var(--green-dark); line-height: 1; }
  .product-copy { position: absolute; left: 216px; top: 342px; width: 340px; font-size: 11.5px; line-height: 14.5px; text-align: justify; color: var(--green-text); }
  .product-copy p + p { margin-top: 14.5px; }
  .turf-roll {
    position: absolute; left: 356px; top: 494px; width: 186px; height: 77px;
    background: linear-gradient(90deg, #7bc43a 0%, #4f9a22 55%, #2f6a17 80%, #3a3a36 100%);
    border-radius: 6px 40px 40px 6px;
  }

  /* Right page */
  .page-right {
    position: absolute; left: 600px; top: 0; width: 600px; height: 600px;
    background: linear-gradient(180deg, #8c959a 0%, #a3acaf 25%, #9da69a 45%, #5f8f3a 62%, #4f8a25 80%, #3d7418 100%);
  }
  .headline-bar { position: absolute; left: 29px; top: 61px; width: 8px; height: 186px; background: var(--rule); }
  .headline { position: absolute; left: 55px; top: 62px; font-size: 35px; font-weight: 400; line-height: 41px; color: var(--white); letter-spacing: 0.3px; }
  .intro { position: absolute; left: 55px; top: 149px; width: 372px; font-size: 13px; line-height: 17px; color: var(--white); }
  .intro p + p { margin-top: 17px; }
</style>
</head>
<body>
<div class="spread">

  <section class="page-left">
    <div class="hero-pool" role="img" aria-label="Foto: Garten mit Pool, Steinterrasse, Pflanzkübeln und Kunstrasen"></div>
    <div class="brand-seal">Halmvollio</div>

    <div class="spec-label" style="top:242px">Farbe</div>
    <div class="spec-value" style="left:29px;top:257px">Sommergrün</div>
    <div class="colour-dots">
      <span style="background:var(--dot-1)"></span>
      <span style="background:var(--dot-2)"></span>
      <span style="background:var(--dot-3)"></span>
      <span style="background:var(--dot-4)"></span>
    </div>

    <div class="spec-label" style="top:325px">Geeignet für</div>
    <ul class="use-list">
      <li>Gärten</li>
      <li>Balkone und Dachterassen</li>
      <li>Innenräume</li>
      <li>Öffentliche Anlagen</li>
    </ul>

    <div class="spec-label" style="top:413px">Florhöhe</div>
    <svg class="pile-icon" width="6" height="36" viewBox="0 0 6 36">
      <line x1="3" y1="2" x2="3" y2="34" stroke="#9aa598" stroke-width="1"/>
      <path d="M0.5 5 L3 1 L5.5 5 M0.5 31 L3 35 L5.5 31" fill="none" stroke="#9aa598" stroke-width="1"/>
    </svg>
    <div class="pile-art" role="img" aria-label="Symbol: Grashalme"></div>
    <div class="spec-value" style="left:67px;top:445px">42mm</div>

    <div class="spec-label" style="top:479px">Gewicht</div>
    <svg class="weight-icon" width="28" height="34" viewBox="0 0 28 34">
      <path d="M8 11 C8 2, 20 2, 20 11" fill="none" stroke="var(--icon-grey)" stroke-width="3"/>
      <ellipse cx="14" cy="22" rx="13.5" ry="11.5" fill="var(--icon-grey)"/>
    </svg>
    <div class="spec-value" style="left:67px;top:508px">2.320 gr/m<sup style="font-size:7px">2</sup></div>

    <div class="spec-label" style="top:545px">Preis</div>
    <div class="spec-value" style="left:29px;top:560px;font-size:12px">35,50 € <span style="font-size:8.5px">zzgl. 19% MwSt</span></div>

    <div class="badge-plain" aria-hidden="true"></div>
    <div class="title-bar"></div>
    <h1 class="product-name">VERDA</h1>
    <h2 class="product-claim">BESTICHT MIT NATÜRLICHER OPTIK</h2>
    <div class="product-copy">
      <p>"Verda" ist ein wundervoller Kunstrasen mit langen, weichen Fasern und einer wunderbar frischen Farbgebung. Mit einer Halmhöhe von 42mm können Sie vor allem Ihren Balkon, Win&shy;tergarten oder Ihre Terasse perfekt in Szene setzen.</p>
      <p>"Verda" besticht durch eine natürliche Optik und vereint die schönen Eigenschaften von Naturrasen mit den techn. Vorzügen unserer Premium Kunstrasen. Ein speziell entwickelter, gekräu&shy;selter, mittellanger Rasen für alle, die Ihre Terasse oder Balkon optisch aufwerten möchten auf dem barfuß Laufen wichtig Spaß macht.</p>
    </div>
    <div class="turf-roll" role="img" aria-label="Foto: aufgerollte Kunstrasenbahn"></div>
  </section>

  <section class="page-right" role="img" aria-label="Foto: Familie liegt gemeinsam auf dem Rasen vor einem modernen Haus">
    <div class="headline-bar"></div>
    <h2 class="headline">GEMEINSAM IM<br>GARTEN ENTSPANNEN.</h2>
    <div class="intro">
      <p>Lassen Sie die mühselige Rasenpflege der Vergangenheit angehören. Mit unserem Premium Kunstrasen können Sie sich im Garten entspannen.</p>
      <p>Widerstandsfähig und langlebig, so hat die ganze Familie etwas davon.</p>
    </div>
  </section>

</div>
</body>
</html>
```